Albeto Wine Label For Harbor Grove

Cedar Bend Winery is in need of a wine label for new wine being release. This wine will be used as a fundraiser for Harbor Grove, a chimpanzee santuary in Georgia. The label should reflect a high-end, classy image and the label should suggest the chimp philanthropy without specifically naming the organization (for legal purposes). The label can be a little whimsical without being too cartoonish or child like. This wine will be sold for $30 so it should project a sense of elegance too.
Updates

holiday season makes it difficult to get feedback necessary for approval. just need a few more days...

Industry/Entity Type

Winery

Font styles to use
Sans Serif

Requirements
Must have
• Label should show common design appearance as other labels downloaded.
• Label should be a dark (emerald) green color. Label should have wine name "Albeto" in center. Label should include an image or silhouette of a chimp on it
Should not have
• no cartoonish images;

```html
<!DOCTYPE html>
<html lang="en">
<head>
<meta charset="utf-8">
<title>Albeto Red Wine Label – Cedar Bend</title>
<link rel="stylesheet" href="https://fonts.googleapis.com/css2?family=Cinzel:wght@700&family=Federo&family=Oswald:wght@400;600&family=Crimson+Text&display=swap">
<style>
  :root {
    --paper: #ffffff;
    --emerald: #1f7a3c;
    --emerald-deep: #17653a;
    --gold: #b08d1b;
    --gold-soft: #c29d28;
    --outline: #1b3d27;
  }
  html, body { margin: 0; padding: 0; overflow: hidden; background: var(--paper); }
  .canvas { position: relative; width: 1200px; height: 999px; overflow: hidden; background: var(--paper); }
  .label-art { position: absolute; inset: 0; }
  .text { position: absolute; color: var(--gold); margin: 0; }

  .brand-mark { left: 90px; top: 262px; width: 160px; display: flex; align-items: center; gap: 10px;
    font: 400 22px/1 "Federo", sans-serif; letter-spacing: 1px; }
  .brand-mark .dot { width: 14px; height: 14px; background: var(--gold); flex: none; }

  .campaign { left: 60px; top: 396px; width: 220px; font: 400 11.5px/14.5px "Crimson Text", serif;
    text-align: justify; color: var(--gold-soft); }
  .campaign p { margin: 0 0 14px; }

  .winery-name { left: 400px; top: 256px; width: 400px; text-align: center; font: 400 58px/1 "Federo", sans-serif; letter-spacing: 2px; }
  .winery-name .sub { display: block; font-size: 36px; margin-top: 2px; letter-spacing: 3px; }
  .wine-name { left: 330px; top: 410px; width: 540px; text-align: center; font: 700 102px/1 "Cinzel", serif; letter-spacing: 1px; }
  .wine-type { left: 400px; top: 508px; width: 400px; text-align: center; font: 700 32px/1 "Cinzel", serif; letter-spacing: 1px; }

  .volume { top: 748px; font: 400 18px/1 "Oswald", sans-serif; letter-spacing: 0.5px; }
  .volume.abv { left: 322px; }
  .volume.size { left: 765px; }

  .warning { left: 922px; top: 228px; width: 222px; font: 400 12.5px/14px "Oswald", sans-serif;
    text-align: justify; text-transform: uppercase; }
  .warning h2 { margin: 0 0 4px; font: 600 17px/1 "Oswald", sans-serif; }
  .warning p { margin: 0 0 8px; }

  .producer { left: 914px; top: 640px; width: 240px; text-align: center; font: 400 16.5px/21px "Oswald", sans-serif; letter-spacing: 0.4px; }
  .website { left: 914px; top: 710px; width: 240px; text-align: center; font: 400 13px/1 "Oswald", sans-serif; }
  .allergen { left: 914px; top: 760px; width: 240px; text-align: center; font: 400 14px/1 "Oswald", sans-serif; }
</style>
</head>
<body>
<div class="canvas">
  <svg class="label-art" width="1200" height="999" viewBox="0 0 1200 999">
    <defs>
      <linearGradient id="panelFill" x1="0" y1="0" x2="1" y2="0">
        <stop offset="0" stop-color="#1d733a"/>
        <stop offset="0.5" stop-color="#1f7b3d"/>
        <stop offset="1" stop-color="#186838"/>
      </linearGradient>
      <linearGradient id="photoFill" x1="0" y1="0" x2="0" y2="1">
        <stop offset="0" stop-color="#3a2a1e"/>
        <stop offset="0.7" stop-color="#2a1d14"/>
        <stop offset="1" stop-color="#3f6a2a"/>
      </linearGradient>
      <clipPath id="diamondInner">
        <polygon points="600,120 860,500 600,880 340,500"/>
      </clipPath>
    </defs>

    <!-- main band -->
    <rect x="18.5" y="188.5" width="1164" height="620" fill="url(#panelFill)" stroke="var(--outline)" stroke-width="1.5"/>
    <rect x="42" y="207" width="1116" height="584" fill="none" stroke="var(--gold)" stroke-width="6"/>
    <rect x="53" y="218" width="1094" height="562" fill="none" stroke="var(--gold)" stroke-width="1.5"/>

    <!-- center diamond -->
    <polygon points="600,82 897,500 600,915 303,500" fill="url(#panelFill)"/>
    <polygon points="600,97 882,500 600,903 318,500" fill="none" stroke="var(--gold)" stroke-width="5"/>
    <polygon points="600,120 860,500 600,880 340,500" fill="none" stroke="var(--gold)" stroke-width="4"/>

    <!-- chimp photograph area -->
    <g clip-path="url(#diamondInner)">
      <rect x="458" y="576" width="292" height="310" rx="40" fill="url(#photoFill)" role="img" aria-label="Photograph of two chimpanzees sitting in grass"/>
    </g>

    <!-- quality badge -->
    <circle cx="1032" cy="540" r="58" fill="var(--gold)"/>
    <circle cx="1032" cy="540" r="44" fill="none" stroke="var(--emerald-deep)" stroke-width="2"/>
  </svg>

  <div class="text brand-mark"><span class="dot"></span>Cedar Bend</div>

  <div class="text campaign">
    <p>A Public awareness campaign designed and dedicated to provide lifetime exemplary care to more than 200 chimpanzees.</p>
    <p>September 14, 2015, marked the effective end of unrestricted invasive experiments on chimpanzees in the United States. All chimps, both wild and captive, were listed as endangered under the Endangered Species Act (ESA) on that day, after a decades-long fight to end the use of chimpanzees in laboratory research.</p>
    <p>We support a forever home sanctuary to all of the chimpanzees in that laboratory research.</p>
    <p>A portion of this wine sale will go to support this campaign.</p>
    <p>Join the Movement.</p>
  </div>

  <h1 class="text winery-name">CEDAR<span class="sub">• BEND •</span></h1>
  <div class="text wine-name">ALBETO</div>
  <div class="text wine-type">Red Wine</div>

  <div class="text volume abv">12.6% ALC./VOL</div>
  <div class="text volume size">750ML</div>

  <div class="text warning">
    <h2>GOVERNMENT WARNING:</h2>
    <p>(1) According to the Surgeon General, women should not drink alcoholic beverages during pregnancy because of the risk of birth defects.</p>
    <p>(2) Consumption of alcoholic beverages impairs your ability to drive a car or operate machinery and may cause health problems.</p>
  </div>

  <div class="text producer">PRODUCED &amp; BOTTLED AT<br>CEDAR BEND RESORT &amp; SPA<br>MAPLE RIDGE GA</div>
  <div class="text website">www.cedarbendga.com</div>
  <div class="text allergen">CONTAIN SULFITES</div>
</div>
</body>
</html>
```